Q-Rolls Business Card

We are a modern retail clothing store. Established in 1994. I need a presentable card that will amaze vendors when given to them.

Front: Logo in middle
Info Side:

Name: Tomas Velder
Cell: 630-812-4463
Work: 630-917-3384 EXT. 417
Email: Tomas@q-rolls-example.com
Website: www.Q-rolls-example.com

Industry/Entity Type

Business

```html
<!DOCTYPE html>
<html lang="en">
<head>
<meta charset="utf-8">
<title>Q-Rolls Business Card</title>
<link rel="stylesheet" href="https://fonts.googleapis.com/css2?family=Montserrat:wght@400;600;700&display=swap">
<style>
  :root {
    --page-bg: #e9e7e3;
    --card-light: #ffffff;
    --card-dark: #000000;
    --pattern-on-light: #c4c4c4;
    --pattern-on-dark: #4a4a4a;
    --ink: #111111;
    --ink-soft: #2b2b2b;
    --paper-text: #ffffff;
    --card-width: 540px;
    --card-height: 309px;
  }
  * { box-sizing: border-box; margin: 0; padding: 0; }
  html, body {
    width: 1200px;
    height: 697px;
    overflow: hidden;
  }
  body {
    background: var(--page-bg);
    font-family: "Montserrat", Arial, sans-serif;
    display: flex;
    align-items: center;
    justify-content: center;
    gap: 40px;
  }
  .card {
    position: relative;
    width: var(--card-width);
    height: var(--card-height);
    overflow: hidden;
    box-shadow: 0 10px 28px rgba(0, 0, 0, 0.18);
  }
  .card--info { background: var(--card-light); }
  .card--front { background: var(--card-dark); }

  .pattern-area {
    position: absolute;
    left: 50%;
    top: 50%;
    width: 360px;
    height: 360px;
    transform: translate(-50%, -50%);
    border-radius: 50%;
  }
  .card--info .pattern-area { background: var(--pattern-on-light); }
  .card--front .pattern-area { background: var(--pattern-on-dark); }

  .center-disc {
    position: absolute;
    left: 50%;
    top: 50%;
    transform: translate(-50%, -50%);
    border-radius: 50%;
  }
  .card--info .center-disc {
    width: 196px;
    height: 196px;
    background: var(--card-light);
  }
  .card--front .center-disc {
    width: 170px;
    height: 170px;
    background: var(--card-dark);
  }

  .contact-list {
    position: absolute;
    left: 50%;
    top: 50%;
    transform: translate(-50%, -50%);
    list-style: none;
    display: flex;
    flex-direction: column;
    gap: 6px;
  }
  .contact-item {
    display: flex;
    align-items: center;
    gap: 7px;
    font-size: 10.5px;
    color: var(--ink-soft);
    white-space: nowrap;
  }
  .contact-icon {
    width: 15px;
    height: 15px;
    flex: none;
  }

  .brand-name {
    position: absolute;
    left: 50%;
    top: 50%;
    transform: translate(-50%, -50%);
    color: var(--paper-text);
    font-weight: 700;
    font-size: 26px;
    letter-spacing: 0.5px;
    text-transform: uppercase;
    white-space: nowrap;
  }
</style>
</head>
<body>

  <section class="card card--info" aria-label="Contact side">
    <div class="pattern-area" role="img" aria-label="Ring of black halftone dots around the contact details"></div>
    <div class="center-disc"></div>
    <ul class="contact-list">
      <li class="contact-item">
        <svg class="contact-icon" viewBox="0 0 16 16" aria-hidden="true"><circle cx="8" cy="8" r="8" fill="#111"/><circle cx="8" cy="6" r="2.2" fill="#fff"/><path d="M4.2 12.2c.6-2.2 2-3.2 3.8-3.2s3.2 1 3.8 3.2z" fill="#fff"/></svg>
        Tomas Velder
      </li>
      <li class="contact-item">
        <svg class="contact-icon" viewBox="0 0 16 16" aria-hidden="true"><circle cx="8" cy="8" r="8" fill="#111"/><rect x="5.5" y="3.5" width="5" height="9" rx="1" fill="none" stroke="#fff" stroke-width="1.2"/><circle cx="8" cy="10.8" r=".6" fill="#fff"/></svg>
        630-812-4463
      </li>
      <li class="contact-item">
        <svg class="contact-icon" viewBox="0 0 16 16" aria-hidden="true"><circle cx="8" cy="8" r="8" fill="#111"/><path d="M5 4.2l1.6-.4 1 2.2-1 .8c.5 1.1 1.3 1.9 2.4 2.4l.8-1 2.2 1-.4 1.6c-3.4.3-6.9-3.2-6.6-6.6z" fill="#fff"/></svg>
        630-917-3384 EXT. 417
      </li>
      <li class="contact-item">
        <svg class="contact-icon" viewBox="0 0 16 16" aria-hidden="true"><circle cx="8" cy="8" r="8" fill="#111"/><rect x="4" y="5" width="8" height="6" fill="none" stroke="#fff" stroke-width="1.1"/><path d="M4 5l4 3.2L12 5" fill="none" stroke="#fff" stroke-width="1.1"/></svg>
        Tomas@q-rolls-example.com
      </li>
      <li class="contact-item">
        <svg class="contact-icon" viewBox="0 0 16 16" aria-hidden="true"><circle cx="8" cy="8" r="8" fill="#111"/><circle cx="8" cy="8" r="4.3" fill="none" stroke="#fff" stroke-width="1"/><ellipse cx="8" cy="8" rx="1.8" ry="4.3" fill="none" stroke="#fff" stroke-width=".9"/><path d="M3.7 8h8.6" stroke="#fff" stroke-width=".9"/></svg>
        www.Q-rolls-example.com
      </li>
    </ul>
  </section>

  <section class="card card--front" aria-label="Front side">
    <div class="pattern-area" role="img" aria-label="Ring of white halftone dots around the company name"></div>
    <div class="center-disc"></div>
    <h1 class="brand-name">Q-Rolls</h1>
  </section>

</body>
</html>
```